A 3d printing services company "The Velvet Lattice" needs a clutter breaking business card design

The Velvet Lattice is a 3d design, animation and printing services company. We are in the B2B and B2C space. www.velvetlattice.com.sg
We have been in business for a year.
The logo is already done (the current file is attached).
We need a business card design which reflects the 3d printing and animations services of the company. A standard rectangular shape is not an option. The card can be die cut.
The card should have the colors of the logo and should have a high tech wow feel to it.
The front of the card should have my name, designation, cellphone email and website details. No need for an office address.
Name: Raghavan Kulkarni
Designation: Founder Director
Cellphone (65)91827345
email: raghavan@velvetlattice.com.sg
website: www.velvetlattice.com.sg
The back of the card should have the services we offer:
1. 3d Design and Modelling
2. 3d Animation
3. 3D Printing
The tag line is: "make your ideas real"
Am uploading the current business card files(back and front).
Target Market(s)
Business owners and C level managers in Marine, Healthcare industry
Industry/Entity Type
Printing
Contact Information for Business Card
Name: Raghavan Kulkarni
Cellphone (65)91827345
2. 3d Animation
3. 3D Printing

```html
<!DOCTYPE html>
<html lang="en">
<head>
<meta charset="utf-8">
<title>The Velvet Lattice – Business Card</title>
<link rel="stylesheet" href="https://fonts.googleapis.com/css2?family=Exo+2:wght@400;600&display=swap">
<style>
  :root {
    --stage: #e6e7e9;
    --paper: #ffffff;
    --brand-green: #3da936;
    --brand-green-light: #9bd67a;
    --brand-blue: #1d63b0;
    --brand-blue-deep: #0c4182;
    --band-grey: #4b4c4e;
    --ink-grey: #55575a;
    --ink-white: #ffffff;
  }
  * { margin: 0; padding: 0; box-sizing: border-box; }
  html, body {
    width: 1200px; height: 898px; overflow: hidden;
    background: var(--stage);
    font-family: "Exo 2", sans-serif;
  }
  .canvas { position: relative; width: 1200px; height: 898px; }

  .card-shadow {
    position: absolute; top: 299px;
    filter: drop-shadow(0 10px 18px rgba(0,0,0,0.18));
  }
  .card-shadow--back { left: 50px; }
  .card-shadow--front { left: 625px; }

  /* die-cut: chamfered top-right and bottom-left corners */
  .card {
    position: relative;
    width: 525px; height: 300px;
    background: var(--paper);
    overflow: hidden;
    clip-path: polygon(0 0, 489px 0, 525px 36px, 525px 300px, 36px 300px, 0 264px);
  }
  .card__art { position: absolute; inset: 0; width: 100%; height: 100%; }

  .logo {
    position: absolute;
    display: flex; align-items: center; gap: 12px;
    white-space: nowrap;
  }
  .logo__dot { border-radius: 50%; background: var(--brand-blue); flex: none; }
  .logo__name { color: var(--brand-green); font-weight: 600; line-height: 1; }

  /* back */
  .card--back .logo { left: 50%; top: 96px; transform: translate(-50%, -50%); }
  .card--back .logo__dot { width: 48px; height: 48px; }
  .card--back .logo__name { font-size: 32px; }
  .tagline {
    position: absolute; left: 0; right: 0; top: 136px;
    text-align: center;
    color: var(--brand-blue);
    font-size: 14px; letter-spacing: 3px; text-transform: uppercase;
  }
  .services {
    position: absolute; left: 0; right: 0; top: 206px;
    display: flex; justify-content: center; gap: 26px;
    list-style: none;
    color: var(--ink-grey);
    font-size: 12.5px; font-weight: 600; letter-spacing: 0.4px;
  }
  .services li { display: flex; align-items: center; gap: 8px; }
  .services li::before {
    content: ""; width: 8px; height: 8px; background: var(--brand-green); flex: none;
  }

  /* front */
  .card--front .logo { left: 50%; top: 60px; transform: translate(-50%, -50%); }
  .card--front .logo__dot { width: 40px; height: 40px; }
  .card--front .logo__name { font-size: 26px; }

  .holder {
    position: absolute; left: 48px; top: 118px;
    color: var(--ink-white);
  }
  .holder__name { font-size: 19px; font-weight: 600; letter-spacing: 1.5px; text-transform: uppercase; line-height: 22px; }
  .holder__role { font-size: 10px; letter-spacing: 1.2px; text-transform: uppercase; margin-top: 2px; }

  .contact {
    position: absolute; left: 300px; top: 170px;
    list-style: none;
    color: var(--ink-white);
    font-size: 10.5px; line-height: 18px; letter-spacing: 0.3px;
  }
</style>
</head>
<body>
<main class="canvas">

  <div class="card-shadow card-shadow--back">
    <section class="card card--back" aria-label="Card back">
      <svg class="card__art" viewBox="0 0 525 300" aria-hidden="true">
        <rect x="0" y="284" width="525" height="16" fill="var(--brand-green)"/>
        <rect x="0" y="278" width="525" height="6" fill="var(--brand-green-light)"/>
      </svg>
      <div class="logo">
        <span class="logo__dot"></span>
        <span class="logo__name">The Velvet Lattice</span>
      </div>
      <p class="tagline">make your ideas real</p>
      <ul class="services">
        <li>3D Design and Modelling</li>
        <li>3D Animation</li>
        <li>3D Printing</li>
      </ul>
    </section>
  </div>

  <div class="card-shadow card-shadow--front">
    <section class="card card--front" aria-label="Card front">
      <svg class="card__art" viewBox="0 0 525 300" aria-hidden="true">
        <defs>
          <linearGradient id="greenBand" x1="0" y1="0" x2="0" y2="1">
            <stop offset="0" stop-color="#5dbd45"/>
            <stop offset="1" stop-color="#35a033"/>
          </linearGradient>
          <linearGradient id="blueTab" x1="0" y1="0" x2="1" y2="1">
            <stop offset="0" stop-color="#2a78c4"/>
            <stop offset="1" stop-color="#0c4182"/>
          </linearGradient>
        </defs>
        <rect class="band band--highlight" x="0" y="98" width="525" height="10" fill="var(--brand-green-light)"/>
        <rect class="band band--name" x="0" y="108" width="525" height="54" fill="url(#greenBand)"/>
        <rect class="band band--grey" x="0" y="162" width="525" height="90" fill="var(--band-grey)"/>
        <polygon class="tab tab--fold" points="290,146 308,146 300,160" fill="var(--brand-blue-deep)"/>
        <polygon class="tab" points="300,146 505,138 495,240 270,262" fill="url(#blueTab)"/>
      </svg>

      <div class="logo">
        <span class="logo__dot"></span>
        <span class="logo__name">The Velvet Lattice</span>
      </div>

      <div class="holder">
        <p class="holder__name">Raghavan Kulkarni</p>
        <p class="holder__role">Founder Director</p>
      </div>

      <ul class="contact">
        <li>(65)91827345</li>
        <li>raghavan@velvetlattice.com.sg</li>
        <li>www.velvetlattice.com.sg</li>
      </ul>
    </section>
  </div>

</main>
</body>
</html>
```